Poster for Office

Looking for an edgy, beautiful poster to hang up in my office that uses the quotes located below and potentially the image attached.
Content for poster

Title: Pell's Rules

Must have the following quotes included (punctuation and capitalization are flexible, do what you think looks the best they also don't need the quotation symbols):

"Don't order fish at a steakhouse"
"Be bold. The more you tell, the more you sell"
"admit nothing, deny everything, launch counterattack."
"avoid obviousness"
"never do anything until you're ready to do it"
"look good=feel good"
"always keep the advantage"
"never complain, never explain"
"Lay low, play dumb, keep moving"

Industry/Entity Type

Quotes

Requirements
Must have
• Title: Pell's Rules

"avoid obviousness"
"look good=feel good"

```html
<!DOCTYPE html>
<html lang="en">
<head>
<meta charset="utf-8">
<title>Pell's Rules</title>
<link rel="stylesheet" href="https://fonts.googleapis.com/css2?family=Della+Respira&display=swap">
<style>
  :root {
    --paper: #ffffff;
    --rust: #b8642a;
    --rust-deep: #6e3a1c;
    --steel-dark: #2b2426;
    --skin-light: #d9cbb0;
    --skin-mid: #a8977a;
    --shadow-navy: #2a2d48;
    --ink: #2a1b10;
    --glow: #d2ac7e;
  }
  html, body {
    margin: 0;
    padding: 0;
    overflow: hidden;
    background: var(--paper);
  }
  .poster {
    position: relative;
    width: 911px;
    height: 1200px;
    overflow: hidden;
    background: var(--paper);
  }
  .backdrop {
    position: absolute;
    inset: 12px 14px 10px 14px;
    border-radius: 18px;
    background:
      radial-gradient(ellipse 48% 60% at 50% 58%, var(--skin-light) 0%, var(--skin-mid) 55%, rgba(168,151,122,0) 82%),
      linear-gradient(180deg, rgba(0,0,0,0) 55%, var(--shadow-navy) 100%),
      linear-gradient(90deg, var(--rust) 0%, var(--rust-deep) 22%, #4a3a36 50%, var(--steel-dark) 78%, #3a3236 100%);
    box-shadow: inset 0 0 40px 22px var(--paper);
  }
  .figure {
    position: absolute;
    left: 200px;
    top: 12px;
    width: 420px;
    height: 400px;
    border-radius: 50% 50% 45% 45% / 40% 40% 60% 60%;
    background: radial-gradient(ellipse at 45% 40%, #b9ab92 0%, #8a7d68 60%, rgba(110,100,88,0) 100%);
    opacity: 0.85;
  }
  .title {
    position: absolute;
    left: 0;
    top: 28px;
    width: 100%;
    margin: 0;
    text-align: center;
    font-family: "Della Respira", serif;
    font-weight: 400;
    font-size: 46px;
    line-height: 1;
    color: var(--ink);
    text-shadow:
      0 0 2px var(--glow), 0 0 3px var(--glow), 0 0 5px var(--glow),
      2px 2px 2px var(--glow), -2px -2px 2px var(--glow),
      2px -2px 2px var(--glow), -2px 2px 2px var(--glow);
  }
  .rules {
    position: absolute;
    left: 0;
    top: 0;
    width: 100%;
    margin: 0;
    padding: 0;
    list-style: none;
  }
  .rule {
    position: absolute;
    left: 0;
    width: 100%;
    text-align: center;
    font-family: "Della Respira", serif;
    font-size: 35px;
    line-height: 1;
    color: var(--ink);
    text-shadow:
      0 0 2px var(--glow), 0 0 3px var(--glow), 0 0 5px var(--glow),
      2px 2px 2px var(--glow), -2px -2px 2px var(--glow),
      2px -2px 2px var(--glow), -2px 2px 2px var(--glow);
    transform: translateY(-50%);
    white-space: nowrap;
  }
</style>
</head>
<body>
  <main class="poster">
    <div class="backdrop" role="img" aria-label="Photograph of a muscular man seen from behind with a smiling portrait tattoo on his upper back, set against rusty and dark diamond-plate metal"></div>
    <div class="figure" role="img" aria-label="Head and shoulders of the man, seen from behind"></div>
    <h1 class="title">Pell's Rules</h1>
    <ul class="rules">
      <li class="rule" style="top:401px">"Don't order fish at a steakhouse"</li>
      <li class="rule" style="top:490px">"Be bold. The more you tell, the more you sell"</li>
      <li class="rule" style="top:579px">"Admit nothing, deny everything, launch counterattack."</li>
      <li class="rule" style="top:668px">"Avoid obviousness"</li>
      <li class="rule" style="top:757px">"Never do anything until you're ready to do it"</li>
      <li class="rule" style="top:845px">"Look Good = Feel Good"</li>
      <li class="rule" style="top:935px">"Always keep the advantage"</li>
      <li class="rule" style="top:1023px">"Never complain, never explain"</li>
      <li class="rule" style="top:1113px">"Lay low, play dumb, keep moving"</li>
    </ul>
  </main>
</body>
</html>
```